Business Card Design

Like white and Blue with gold border

Industry/Entity Type

Business

Contact Information for Business Card

CLEARWAY TAX AND ACCOUNTING SERVICE
Registered Tax Agent
PO Box 815 or 167 Marlowe Street Rockhampton Q. 4700
Phone 07 41563092
Fax 07 41568417
clearwaytax@voskerhall.com
Senior Tax Preparer - MAREE COLWILL

Requirements
Must have
• on back of card should have - Appointment Date and time

```html
<!DOCTYPE html>
<html lang="en">
<head>
<meta charset="utf-8">
<title>Clearway Tax and Accounting Service – Appointment Card</title>
<link rel="stylesheet" href="https://fonts.googleapis.com/css2?family=Open+Sans:ital,wght@0,400;0,600;0,700;1,700&display=swap">
<style>
  :root {
    --navy: #0c2a5c;
    --gold-deep: #de8c0c;
    --gold-light: #f7dc72;
    --gold-mid: #ecb53a;
    --paper: #ffffff;
  }
  * { margin: 0; padding: 0; box-sizing: border-box; }
  html, body {
    width: 1200px;
    height: 741px;
    overflow: hidden;
    background: var(--paper);
  }
  .card {
    position: relative;
    width: 1200px;
    height: 741px;
    background: var(--paper);
    font-family: "Open Sans", Arial, sans-serif;
    color: var(--navy);
  }
  .card-frame {
    position: absolute;
    inset: 0;
  }
  .brand {
    position: absolute;
    top: 72px;
    left: 0;
    width: 100%;
    display: flex;
    flex-direction: column;
    align-items: center;
  }
  .brand-dot {
    width: 214px;
    height: 214px;
    border-radius: 50%;
    background: var(--gold-mid);
  }
  .brand-name {
    margin-top: 58px;
    font-size: 29px;
    font-weight: 600;
    letter-spacing: 0.01em;
    color: var(--navy);
  }
  .appointment-title {
    position: absolute;
    top: 458px;
    width: 100%;
    text-align: center;
    font-size: 33px;
    font-weight: 700;
    letter-spacing: 0.01em;
  }
  .appointment-fields {
    position: absolute;
    top: 546px;
    left: 85px;
    display: flex;
    align-items: baseline;
    font-size: 32px;
    font-weight: 400;
  }
  .field { display: flex; align-items: baseline; }
  .field + .field { margin-left: 22px; }
  .field-line {
    display: inline-block;
    width: 402px;
    height: 1px;
    margin-left: 10px;
    border-bottom: 3px dotted var(--navy);
  }
  .tagline {
    position: absolute;
    top: 638px;
    left: 87px;
    font-size: 22px;
    font-weight: 700;
    font-style: italic;
    letter-spacing: 13.4px;
    white-space: nowrap;
  }
</style>
</head>
<body>
<main class="card">
  <svg class="card-frame" width="1200" height="741" viewBox="0 0 1200 741" aria-hidden="true">
    <defs>
      <linearGradient id="frame-gold" x1="0" y1="0" x2="1" y2="0">
        <stop offset="0" stop-color="#de8c0c"/>
        <stop offset="0.2" stop-color="#f7dc72"/>
        <stop offset="0.45" stop-color="#de8c0c"/>
        <stop offset="0.7" stop-color="#f7dc72"/>
        <stop offset="1" stop-color="#de8c0c"/>
      </linearGradient>
    </defs>
    <rect x="34" y="30" width="1138" height="681" rx="52" ry="52"
          fill="none" stroke="url(#frame-gold)" stroke-width="15"/>
  </svg>

  <header class="brand">
    <div class="brand-dot" aria-hidden="true"></div>
    <p class="brand-name">CLEARWAY TAX AND ACCOUNTING SERVICE</p>
  </header>

  <h1 class="appointment-title">APPOINTMENT</h1>

  <section class="appointment-fields">
    <div class="field"><span class="field-label">Date:</span><span class="field-line"></span></div>
    <div class="field"><span class="field-label">Time:</span><span class="field-line"></span></div>
  </section>

  <p class="tagline">CLEARWAY BY NAME BUT BEST IN SERVICE</p>
</main>
</body>
</html>
```